Brightwell Bonds and Households Initiative

We need a flyer that invites low-income Spanish speaking individuals to our program. The program is 12 weeks. We offer healthy relationship education, and financial stability. We also touch on workforce development. These workshops are for couples only.

We are in five locations, so we need a flyer that we can change the text to be able to update the address, dates and any additional information based on our needs.

Attached is the logo we would like to use. I have also attached a previous flyer that we created to give you an idea of the text that is included.

Target Market(s)

We are reaching out to low income adult couples

Font styles to use
Serif

Requirements
Must have
• This flyer must catch the eye of couples wanting to improve their relationship, and finances.
Nice to have
• Some space for us to plug in dates location and times. This flyer also has to have our funding statement at the bottom.

```html
<!DOCTYPE html>
<html lang="es">
<head>
<meta charset="utf-8">
<title>Talleres para Parejas</title>
<link href="https://fonts.googleapis.com/css2?family=Archivo+Black&family=Arimo:ital,wght@0,400;0,700;1,400;1,700&family=Open+Sans:wght@400;600&display=swap" rel="stylesheet">
<style>
  :root {
    --frame: #1b1b1b;
    --paper: #ffffff;
    --green: #22a84a;
    --navy: #1d2a3a;
    --orange: #f08a24;
    --soft-white: #eef7ee;
    --badge: #ffffff;
  }
  * { margin: 0; padding: 0; box-sizing: border-box; }
  html, body { width: 894px; height: 1200px; overflow: hidden; background: var(--frame); }
  .flyer { position: relative; width: 894px; height: 1200px; font-family: "Arimo", Arial, sans-serif; }
  .backdrop { position: absolute; inset: 0; }
  .block { position: absolute; }

  .brand { left: 62px; top: 104px; width: 400px; }
  .brand-name { display: flex; align-items: center; gap: 8px; font-family: "Arimo", Arial, sans-serif; font-weight: 700; font-size: 18px; color: var(--orange); line-height: 1.15; }
  .brand-dot { width: 14px; height: 14px; border-radius: 50%; background: var(--orange); flex: none; }
  .brand-sub { margin-top: 8px; font-family: "Arimo", Arial, sans-serif; font-weight: 700; font-size: 8.6px; letter-spacing: 0.4px; color: var(--navy); text-align: center; line-height: 1.2; text-transform: uppercase; }

  .tagline { left: 480px; top: 126px; width: 370px; text-align: center; font-style: italic; font-weight: 700; font-size: 21px; line-height: 1.35; color: #111; }

  .headline { left: 58px; top: 230px; color: var(--navy); font-family: "Archivo Black", "Arial Black", sans-serif; line-height: 1; }
  .headline-top { font-size: 40px; letter-spacing: 0.5px; }
  .headline-main { font-size: 71px; letter-spacing: 1px; margin-top: 2px; }

  .topics { left: 58px; top: 380px; width: 400px; }
  .topics-title { font-family: "Open Sans", Arial, sans-serif; font-weight: 600; font-size: 17px; color: var(--navy); margin-bottom: 4px; }
  .topics-list { list-style: none; font-family: "Open Sans", Arial, sans-serif; font-size: 12.6px; color: var(--soft-white); line-height: 18px; }
  .topics-list li::before { content: "\25C6"; color: var(--navy); font-size: 8px; margin: 0 9px 0 4px; vertical-align: 2px; }

  .register { left: 58px; top: 570px; width: 380px; }
  .register-title { font-family: "Archivo Black", "Arial Black", sans-serif; font-size: 18px; color: var(--navy); line-height: 22px; }
  .register-text { margin-top: 6px; font-size: 14.5px; color: var(--paper); line-height: 20px; }

  .details { left: 63px; top: 700px; width: 320px; font-size: 18.5px; line-height: 20px; color: var(--paper); }
  .details-label { font-weight: 700; color: var(--navy); text-decoration: underline; }
  .details-venue { font-style: italic; }
  .details-note { margin-top: 26px; }

  .funding { left: 62px; top: 1017px; width: 300px; font-family: "Open Sans", Arial, sans-serif; font-size: 10.3px; line-height: 15px; color: var(--paper); }

  .partner-badge { position: absolute; left: 718px; width: 114px; height: 78px; border-radius: 10px; background: var(--badge); }
  .partner-badge.first { top: 941px; }
  .partner-badge.second { top: 1028px; }
</style>
</head>
<body>
<div class="flyer">
  <svg class="backdrop" width="894" height="1200" viewBox="0 0 894 1200">
    <defs>
      <linearGradient id="photoTone" x1="0" y1="0" x2="0" y2="1">
        <stop offset="0" stop-color="#f2f3f0"/>
        <stop offset="0.14" stop-color="#b9bcb0"/>
        <stop offset="0.3" stop-color="#6b5a48"/>
        <stop offset="0.55" stop-color="#3a2a20"/>
        <stop offset="1" stop-color="#17110d"/>
      </linearGradient>
      <linearGradient id="gownTone" x1="0" y1="0" x2="0" y2="1">
        <stop offset="0" stop-color="#cfc9c0" stop-opacity="0"/>
        <stop offset="1" stop-color="#e9e6e1" stop-opacity="0.8"/>
      </linearGradient>
    </defs>
    <rect x="37" y="70" width="820" height="1061" fill="var(--paper)"/>
    <g role="img" aria-label="Photo of a bride and groom embracing outdoors, looking into the distance">
      <rect x="420" y="70" width="437" height="1061" fill="url(#photoTone)"/>
      <rect x="420" y="980" width="280" height="151" fill="url(#gownTone)"/>
    </g>
    <rect x="37" y="70" width="420" height="113" fill="var(--paper)"/>
    <path d="M37,183 L455,183 C495,220 502,280 497,350 C492,440 500,520 462,600 C422,680 382,760 367,850 C356,950 370,1060 372,1131 L37,1131 Z" fill="var(--green)"/>
  </svg>

  <div class="block brand">
    <div class="brand-name"><span class="brand-dot"></span>Brightwell Bonds and Households Initiative</div>
    <div class="brand-sub">Fortalecimiento de Relaciones | Capacitación Financiera<br>y Preparacion Laboral</div>
  </div>

  <div class="block tagline">Porque una relación sana esta<br>“A Nuestro Alcance”</div>

  <div class="block headline">
    <div class="headline-top">TALLERES PARA</div>
    <div class="headline-main">PAREJAS</div>
  </div>

  <div class="block topics">
    <div class="topics-title">Temas incluyen:</div>
    <ul class="topics-list">
      <li>Llaves para la buena communicación</li>
      <li>Tipos de personalidad y expectativas</li>
      <li>Señales de peligro en una relación</li>
      <li>Técnicas para formar y sostener una relación sana</li>
      <li>Resolucion de problemas</li>
      <li>Como mantener la diversion</li>
      <li>Como adminstrar el dinero entre pareja Y muchos mas</li>
    </ul>
  </div>

  <div class="block register">
    <div class="register-title">Registración requerida<br>Llámanos hoy!</div>
    <div class="register-text">Para más información llame a Willow Creek<br>Family Resource Center. (555) 201-4470</div>
  </div>

  <div class="block details">
    <div class="details-label">Fecha de talleres:</div>
    <div>jueves octubre 03, 12, 19, 26</div>
    <div class="details-label">Horario:</div>
    <div>5:30pm –8:00pm</div>
    <div class="details-label">Ubicación:</div>
    <div><span class="details-venue">Willow Creek Family Resource Center</span> 2850 Alder Ave,<br>Fairview CA 90210<br>(555) 201-4412</div>
    <div class="details-note">*Cuidado de niños y cena será proporcionado</div>
  </div>

  <div class="block funding">“Funding for this project was provided by the National Family Services Agency, Office of Children and Families, Grant: #90ZZ0000. These services are available to all eligible persons, regardless of race, gender, age, disability, or religion.”</div>

  <div class="partner-badge first" role="img" aria-label="Partner badge"></div>
  <div class="partner-badge second" role="img" aria-label="Partner badge"></div>
</div>
</body>
</html>
```